TIPSY PANTRY needs a show poster

"Tipsy Pantry" is a stand up comedy show. We need a fun, eye-catching poster. The taglines are "Heaps of Giggles" and "Fresh Jokes, Shaken Cocktails." We are attaching our logo files and a vintage photo that we sometimes use, but they do not need to be a part of the poster. We like vintage* and retro* images but are open to the creativity of the designer.

* Added note: Vintage and Retro to us means 1950s-1970s design types, not distressed and worn looking. Color is good!

Target Market(s)

Women & Couples, Ages 30-70

Industry/Entity Type

Comedy

Requirements
Must have
• Title: Tipsy Pantry
• Primary Tagline: Loads of Laughs
• Performers Names: Helen Forsyth & Joan Pettibrook
Nice to have
• Secondary Tagline: Fresh Jokes, Shaken Cocktails.
Should not have
• No cliche images of stand up comedy (spotlight, stage, microphone)

```html
<!DOCTYPE html>
<html lang="en">
<head>
<meta charset="utf-8">
<title>Tipsy Pantry – Heaps of Giggles</title>
<link rel="stylesheet" href="https://fonts.googleapis.com/css2?family=Alfa+Slab+One&family=Anton&family=Bangers&display=swap">
<style>
  :root {
    --blue-deep: #0b2a8f;
    --blue-mid: #1f5fd6;
    --blue-light: #3fa2ee;
    --ink: #121212;
    --white: #ffffff;
    --orange: #f47a12;
    --yellow: #fff23a;
    --red: #e0323a;
    --popcorn-cream: #fff6d8;
    --popcorn-butter: #f6c12c;
  }
  html, body {
    margin: 0;
    padding: 0;
    overflow: hidden;
    background: #e9e9e9;
  }
  .poster {
    position: relative;
    width: 855px;
    height: 1200px;
    overflow: hidden;
    background: radial-gradient(ellipse at 50% 45%, var(--blue-light) 0%, var(--blue-mid) 40%, var(--blue-deep) 100%);
    font-family: "Anton", sans-serif;
  }
  .brand {
    position: absolute;
    left: 0;
    right: 0;
    top: 170px;
    margin: 0;
    text-align: center;
    font-family: "Anton", sans-serif;
    font-weight: 400;
    font-size: 62px;
    line-height: 70px;
    letter-spacing: 2px;
    color: var(--white);
  }
  .title-art {
    position: absolute;
    left: 0;
    top: 0;
    width: 855px;
    height: 1200px;
  }
  .title-main {
    font-family: "Alfa Slab One", serif;
  }
  .tagline-text {
    font-family: "Anton", sans-serif;
  }
  .performers-label {
    position: absolute;
    left: 333px;
    top: 836px;
    width: 238px;
    height: 48px;
    background: var(--yellow);
    border: 4px solid var(--red);
    box-sizing: border-box;
    transform: rotate(-2deg);
    text-align: center;
    font-family: "Anton", sans-serif;
    font-size: 30px;
    line-height: 40px;
    color: var(--ink);
  }
  .popcorn {
    position: absolute;
    left: -40px;
    right: -40px;
    bottom: -60px;
    height: 330px;
    border-radius: 50% 50% 0 0 / 40% 40% 0 0;
    background: radial-gradient(ellipse at 50% 20%, var(--popcorn-cream) 0%, var(--white) 45%, var(--popcorn-butter) 100%);
  }
  .performers {
    position: absolute;
    left: 0;
    right: 0;
    top: 900px;
    margin: 0;
    text-align: center;
    font-family: "Bangers", sans-serif;
    font-weight: 400;
    font-size: 96px;
    line-height: 96px;
    letter-spacing: 1px;
    color: var(--orange);
    -webkit-text-stroke: 3px var(--ink);
    text-shadow: 5px 5px 0 var(--white), -3px -3px 0 var(--white), 3px -3px 0 var(--white), -3px 3px 0 var(--white);
    transform: rotate(-3deg);
  }
</style>
</head>
<body>
<div class="poster">
  <h2 class="brand">TIPSY PANTRY</h2>

  <svg class="title-art" viewBox="0 0 855 1200" aria-labelledby="title-heading">
    <title id="title-heading">Heaps of Giggles</title>
    <!-- title plate -->
    <polygon points="78,328 740,320 790,716 50,752" fill="var(--white)"/>
    <polygon points="92,342 726,334 772,704 66,736" fill="var(--ink)"/>
    <text class="title-main" x="120" y="505" font-size="150" fill="var(--orange)" textLength="480" lengthAdjust="spacingAndGlyphs">HEAPS</text>
    <rect x="634" y="392" width="92" height="92" fill="var(--yellow)"/>
    <text class="title-main" x="680" y="458" font-size="50" fill="var(--ink)" text-anchor="middle">OF</text>
    <text class="title-main" x="108" y="676" font-size="140" fill="var(--yellow)" textLength="645" lengthAdjust="spacingAndGlyphs">GIGGLES</text>
    <!-- tagline band -->
    <polygon points="58,762 792,718 800,792 72,836" fill="var(--white)"/>
    <polygon points="70,770 782,728 790,784 82,826" fill="var(--ink)"/>
    <text class="tagline-text" x="430" y="798" font-size="52" fill="var(--white)" text-anchor="middle" transform="rotate(-3.4 430 780)" textLength="650" lengthAdjust="spacingAndGlyphs">FRESH JOKES, SHAKEN COCKTAILS</text>
    <!-- dashes beside the label -->
    <g stroke="var(--white)" stroke-width="6" stroke-linecap="round">
      <line x1="222" y1="852" x2="310" y2="848"/>
      <line x1="216" y1="866" x2="312" y2="862"/>
      <line x1="222" y1="880" x2="310" y2="876"/>
      <line x1="592" y1="838" x2="680" y2="834"/>
      <line x1="590" y1="852" x2="686" y2="848"/>
      <line x1="592" y1="866" x2="680" y2="862"/>
    </g>
  </svg>

  <div class="performers-label">PERFORMERS</div>

  <div class="popcorn" role="img" aria-label="Illustrated pile of popcorn filling the bottom of the poster"></div>

  <h1 class="performers">HELEN FORSYTH &amp;<br>JOAN PETTIBROOK</h1>
</div>
</body>
</html>
```